Bold Modern Creative Wine Label Needed for a Chardonnay

We need a modern, eye catching label, one that will appeal to millennials, but also attract the older more conservative crowd. We like the boldness of black on white but are open to your suggestions. Since the bottle type is a light green 'burgundy style' bottle, you should take that into account. The name of the brand is Vo`. The attached label is example of what we like very much. It is eye catching and bold and modern. Keep in mind that the bottle will be light green in color so black and white might not work so well. Use your creativity please! The label can be any size but needs to fit on this shape bottle. See attached photos. thanks!!

(Please no grapes or wine glasses or wine bottles featured on the label!)
Updates

Hi Designers, I just wanted to let you know that we received many great designs and we are sorting through them this week. The website is making it a bit difficult to create a 'poll' so this is taking longer than we expected. Thanks for all the great submissions!

```html
<!DOCTYPE html>
<html lang="en">
<head>
<meta charset="UTF-8">
<title>Vo` Chardonnay Label</title>
<link rel="stylesheet" href="https://fonts.googleapis.com/css2?family=EB+Garamond:wght@400&display=swap">
<style>
  :root {
    --backdrop: #f3f3ef;
    --label-cream: #fcfbe1;
    --stripe-yellow: #f7f1be;
    --ink-olive: #4b4632;
  }
  * { margin: 0; padding: 0; box-sizing: border-box; }
  html, body {
    width: 690px;
    height: 1200px;
    overflow: hidden;
    background: var(--backdrop);
  }
  .canvas {
    position: relative;
    width: 690px;
    height: 1200px;
  }
  .wine-label {
    position: absolute;
    left: 45px;
    top: 327px;
    width: 600px;
    height: 545px;
    background: var(--label-cream);
    font-family: "EB Garamond", "Times New Roman", serif;
    font-weight: 400;
    color: var(--ink-olive);
    box-shadow: 0 2px 10px rgba(0, 0, 0, 0.06);
  }
  .label-stripe {
    position: absolute;
    left: 130px;
    top: 0;
    width: 28px;
    height: 100%;
    background: var(--stripe-yellow);
  }
  .brand-name {
    position: absolute;
    left: 196px;
    top: 110px;
    font-size: 110px;
    line-height: 1;
    white-space: nowrap;
  }
  .winery-name {
    position: absolute;
    left: 198px;
    top: 370px;
    font-size: 28px;
    line-height: 1.2;
    letter-spacing: 0.5px;
    white-space: nowrap;
  }
  .rule {
    position: absolute;
    height: 3px;
    background: var(--ink-olive);
  }
  .rule-upper { left: 192px; top: 410px; width: 400px; }
  .rule-lower { left: 0; top: 463px; width: 437px; }
  .since-year {
    position: absolute;
    left: 258px;
    top: 425px;
    font-size: 21px;
    line-height: 1.2;
    letter-spacing: 0.5px;
    white-space: nowrap;
  }
  .volume-info {
    position: absolute;
    left: 143px;
    top: 484px;
    font-size: 22px;
    line-height: 1.2;
    white-space: nowrap;
  }
</style>
</head>
<body>
  <main class="canvas">
    <section class="wine-label">
      <div class="label-stripe"></div>
      <h1 class="brand-name">Vo`</h1>
      <p class="winery-name">By VO WINERY</p>
      <div class="rule rule-upper"></div>
      <p class="since-year">SINCE 2009</p>
      <div class="rule rule-lower"></div>
      <p class="volume-info">12% ALC VOL 750ml</p>
    </section>
  </main>
</body>
</html>
```